Website concept design - need very creative and polished web page layouts

Need 3-4 web pages designed (graphic only). Client is an interior designer and has specific design requirements. Need a skilled graphic designer to help me create a concept for the new site.

The site is primarily meant to allow users to build and buy a new product, but should have a portfolio site feel. I have specific requirements so designer won't have to 'figure it out' on their own.

Making use of white space, text orientation, and object movement are essential to the success of this project.

Inspirational sites:

http://brisk.tamo.site/#en - creative and atypical
https://pembly.io/ - white space and movement; vertical menu links
https://738q.jp- modern into, object hover movement
https://www.polnaxo.com/case-copper-reed - white space, dimensional feel of objects floating on page; pop of color

Target Market(s)

Interior designers and individuals - both commercial and retail.

Industry/Entity Type

Interior Design

Number of Pages Required

4 page

Font styles to use
Serif
Sans Serif

Requirements
Must have
• Professional design, meet design requirements, professional and highly creative look. This cannot look like or resemble in any way a common or typical website. Making use of white space, text orientation, and object movement are essential to the success of this project.
• Colors for the project:
• COLOR TREATMENT - (Not Final)
• DARK PUTTY – 77% Black
• R 95
• G 96
• B 98
• LIGHT PUTTY – 50% Black
• R 129
• G 131
• B 134
• ** Other Levels of Putty can be used.
• BLUE GREEN - (May not be final)
• R 113
• G 202
• B 210
Should not have
• Cannot look like or resemble a typical website design.

```html
<!DOCTYPE html>
<html lang="en">
<head>
<meta charset="utf-8">
<title>Tessel Lamp – About</title>
<link href="https://fonts.googleapis.com/css2?family=Lato:wght@400;700&display=swap" rel="stylesheet">
<style>
  :root {
    --dark-putty: #5f6062;
    --light-putty: #818386;
    --mid-putty: #6e6f72;
    --blue-green: #71cad2;
    --paper: #ffffff;
    --mist: #ececec;
    --line: #c9cacc;
  }
  * { margin: 0; padding: 0; box-sizing: border-box; }
  html, body { width: 1200px; height: 763px; overflow: hidden; background: var(--paper); }
  body { font-family: "Lato", Arial, sans-serif; color: var(--dark-putty); position: relative; }

  .backdrop { position: absolute; inset: 0; }

  .site-header { position: absolute; top: 0; left: 0; width: 1200px; height: 80px; }
  .brand {
    position: absolute; left: 120px; top: 30px;
    font-size: 36px; font-weight: 400; letter-spacing: 1px; color: var(--mid-putty);
  }
  .search {
    position: absolute; left: 572px; top: 34px; width: 234px; height: 32px;
    border: 1px solid var(--line); border-radius: 16px;
    display: flex; align-items: center; padding-left: 14px; gap: 8px;
    font-size: 11px; color: var(--light-putty);
  }
  .phone {
    position: absolute; left: 833px; top: 37px;
    display: flex; align-items: center; gap: 5px;
    font-size: 16px; color: var(--dark-putty);
  }
  .cart {
    position: absolute; left: 988px; top: 30px; width: 37px; height: 37px;
    border: 2px solid var(--light-putty); border-radius: 50%;
    display: flex; align-items: center; justify-content: center;
  }
  .menu-toggle { position: absolute; left: 1052px; top: 40px; width: 30px; }
  .menu-toggle span { display: block; height: 2px; background: var(--light-putty); margin-bottom: 4px; }

  .about-card {
    position: absolute; left: 101px; top: 211px; width: 498px; height: 322px;
    border: 1px solid var(--blue-green); background: var(--paper);
    text-align: center;
  }
  .about-card h1 {
    font-weight: 400; font-size: 35px; margin-top: 42px; letter-spacing: 0;
    color: var(--dark-putty);
  }
  .about-card p { font-size: 16.5px; line-height: 22px; margin-top: 12px; }
  .about-card p + p { margin-top: 13px; }
  .read-more {
    display: inline-block; margin-top: 20px; width: 166px; height: 42px; line-height: 42px;
    background: var(--dark-putty); color: var(--paper); font-size: 15.5px; text-decoration: none;
  }

  .lamp { position: absolute; }
  .lamp-pattern {
    left: 634px; top: 295px; width: 173px; height: 321px;
    background: linear-gradient(180deg, #69696b 0%, #707072 40%, #9a9a9c 60%, #8b8b8e 100%);
    border-radius: 6px 6px 14px 14px;
  }
  .lamp-stripe {
    left: 828px; top: 190px; width: 258px; height: 407px;
    background: linear-gradient(180deg, #fafafa 0%, #f3f3f3 55%, #6b6a68 62%, #c9c9c9 80%, #a9aaae 100%);
  }

  .site-footer .copyright {
    position: absolute; left: 129px; top: 708px; font-size: 13px; color: var(--light-putty);
  }
  .social { position: absolute; left: 438px; top: 708px; display: flex; gap: 32px; }
  .social a { display: block; width: 16px; height: 16px; border-radius: 50%; background: var(--blue-green); }
</style>
</head>
<body>
  <svg class="backdrop" width="1200" height="763" viewBox="0 0 1200 763" aria-hidden="true">
    <defs>
      <linearGradient id="topFade" x1="0" y1="0" x2="0" y2="1">
        <stop offset="0" stop-color="#e8e8e8"/>
        <stop offset="1" stop-color="#ffffff"/>
      </linearGradient>
      <linearGradient id="bottomFade" x1="0" y1="0" x2="0" y2="1">
        <stop offset="0" stop-color="#ffffff"/>
        <stop offset="1" stop-color="#e6e6e6"/>
      </linearGradient>
    </defs>
    <polygon points="0,81 1200,110 1200,200 0,180" fill="url(#topFade)"/>
    <polygon points="0,590 1200,610 1200,722 0,696" fill="url(#bottomFade)"/>
    <polygon points="792,107 1200,81 1200,103" fill="#818386"/>
    <polygon points="672,110 1200,103 1200,136" fill="#71cad2"/>
    <polygon points="0,649 206,660 0,696" fill="#5f6062"/>
  </svg>

  <header class="site-header">
    <div class="brand">TESSEL LAMP</div>
    <div class="search">
      <svg width="15" height="15" viewBox="0 0 16 16" aria-hidden="true">
        <circle cx="6.5" cy="6.5" r="5" fill="none" stroke="#c9cacc" stroke-width="2"/>
        <line x1="10.5" y1="10.5" x2="15" y2="15" stroke="#c9cacc" stroke-width="2.2"/>
      </svg>
      Search here
    </div>
    <div class="phone">
      <svg width="19" height="19" viewBox="0 0 24 24" aria-hidden="true">
        <path fill="#71cad2" d="M6.6 10.8a15.1 15.1 0 0 0 6.6 6.6l2.2-2.2c.3-.3.7-.4 1-.2 1.1.4 2.3.6 3.6.6.6 0 1 .4 1 1V20c0 .6-.4 1-1 1A17 17 0 0 1 3 4c0-.6.4-1 1-1h3.5c.6 0 1 .4 1 1 0 1.3.2 2.5.6 3.6.1.3 0 .7-.2 1z"/>
      </svg>
      (800).555.0142
    </div>
    <div class="cart">
      <svg width="18" height="16" viewBox="0 0 24 22" aria-hidden="true">
        <path fill="#71cad2" d="M1 1h4l1 3h17l-3 9H8l-1 2h13v2H4l2.5-4.5L3.5 3H1z"/>
        <circle cx="8" cy="20" r="1.8" fill="#71cad2"/>
        <circle cx="18" cy="20" r="1.8" fill="#71cad2"/>
      </svg>
    </div>
    <div class="menu-toggle"><span></span><span></span><span></span></div>
  </header>

  <main>
    <section class="about-card">
      <h1>ABOUT TESSEL LAMP</h1>
      <p>Morbi diam mauris viverra in gravida eu mattis in ante<br>Morbi eget arcu Morbi porta libero id ullamcorper</p>
      <p>nonummy nibh ligula pulvinar metus eget consectetuer<br>augue nisi quis lacus Ut ac mi quis lacus mollis aliquam<br>Curabitur iaculis tempus eros Curabitur ve mi</p>
      <a class="read-more" href="#">READ MORE</a>
    </section>
    <div class="lamp lamp-pattern" role="img" aria-label="Table lamp with grey drum shade and lattice-patterned ceramic base"></div>
    <div class="lamp lamp-stripe" role="img" aria-label="Table lamp with white rectangular shade and grey striped square base"></div>
  </main>

  <footer class="site-footer">
    <div class="copyright">© 2018 Company Name&nbsp;&nbsp;All right reserved</div>
    <nav class="social" aria-label="Social links">
      <a href="#" aria-label="Social link one"></a>
      <a href="#" aria-label="Social link two"></a>
      <a href="#" aria-label="Social link three"></a>
      <a href="#" aria-label="Social link four"></a>
    </nav>
  </footer>
</body>
</html>
```